Varlow Landscaping

Create a website for a new landscaping company. I have a logo already and description of services offered. I have a website that I would like all inquiries and appointments to get forwarded to. I need just need it well organized so that a husband and wife team can manage it easily. This is a company that will continue to grow over time and will need to add more services under new tabs over time. If you need the email where appointments and inquiries should go please send me a message.
Services offered are: Weekly/bi weekly mowing, weed eating and edging, Plant installation pinestraw & mulch installation, weed & feed, leaf removal and yard clean up.

```html
<!DOCTYPE html>
<html lang="en">
<head>
<meta charset="utf-8">
<title>Varlow Landscaping</title>
<link rel="stylesheet" href="https://fonts.googleapis.com/css2?family=Montserrat:wght@400;500;600;700;800;900&display=swap">
<style>
:root{
  --green:#7cbf2f;
  --green-dark:#4f9a1c;
  --green-deep:#2f6d12;
  --yellow:#f5c518;
  --beige:#f2f0e8;
  --ink:#1f2a1a;
  --muted:#6b6f66;
  --white:#ffffff;
  --line:#dcdcd4;
}
*{box-sizing:border-box;margin:0;padding:0}
html,body{width:1200px;height:4716px;overflow:hidden;background:var(--white)}
body{font-family:"Montserrat",sans-serif;color:var(--ink);position:relative}
section,header,footer{position:absolute;left:0;width:1200px;overflow:hidden}
.abs{position:absolute}
.btn{position:absolute;display:inline-flex;align-items:center;gap:10px;border-radius:22px;font-weight:700;font-size:12px;letter-spacing:.5px;padding:0 8px 0 20px;height:40px;white-space:nowrap;width:auto}
.btn .dot{width:26px;height:26px;border-radius:50%;background:var(--white);display:flex;align-items:center;justify-content:center}
.btn-yellow{background:var(--yellow);color:var(--ink)}
.btn-green{background:var(--green);color:var(--white)}
.section-title{position:absolute;width:100%;text-align:center;font-weight:800;font-size:34px;letter-spacing:.5px}
.small{font-size:12px;line-height:1.65;color:var(--muted)}

/* header / hero */
.hero{top:0;height:660px}
.hero-photo{position:absolute;inset:0;background:linear-gradient(120deg,#3f6b1e 0%,#7ea83a 35%,#d9c45a 58%,#9cbc4a 72%,#4d7a22 100%)}
.nav-bar{position:absolute;top:0;left:0;width:1200px;height:72px;background:var(--white)}
.nav-links{position:absolute;left:404px;top:0;height:72px;display:flex;align-items:center;gap:40px;font-size:11px;font-weight:600}
.nav-links .active{color:var(--green-dark);border-bottom:2px solid var(--green);padding-bottom:4px}
.nav-cta{right:110px;top:18px;font-size:10px;height:36px;padding-left:16px}
.brand-badge{position:absolute;left:112px;top:-10px;width:150px;height:150px;border-radius:50%;background:var(--white);border:5px solid var(--green);display:flex;flex-direction:column;align-items:center;justify-content:center;z-index:2}
.brand-name{font-weight:900;color:var(--green-dark);font-size:24px;letter-spacing:1px}
.brand-sub{font-weight:700;font-size:8px;color:var(--green-dark);margin-top:2px}
.hero-title{position:absolute;left:120px;top:226px;width:620px;color:var(--white);font-weight:900;font-size:44px;line-height:1.12}
.hero-sub{position:absolute;left:120px;top:390px;width:280px;color:var(--white);font-size:11px;font-weight:600;line-height:1.5}
.hero-cta{left:120px;top:462px}
.slider-dots{position:absolute;left:126px;top:604px;display:flex;gap:8px}
.slider-dots span{width:10px;height:10px;border-radius:50%;background:rgba(255,255,255,.6)}
.slider-dots span:first-child{background:var(--white)}

/* about */
.about{top:660px;height:552px}
.about-photo{position:absolute;left:220px;top:80px;width:390px;height:390px;border-radius:50%;background:radial-gradient(circle at 50% 40%,#a6cf5a,#4d8a22 75%);border:6px solid var(--white);box-shadow:0 0 0 3px var(--green)}
.about-photo-sm{position:absolute;left:160px;top:320px;width:160px;height:160px;border-radius:50%;background:linear-gradient(160deg,#8fbf4a,#3d7318);border:6px solid var(--white)}
.about-title{position:absolute;left:660px;top:150px;font-weight:800;font-size:28px;line-height:1.15}
.about-title .hl{color:var(--green-dark)}
.about-text{position:absolute;left:660px;top:230px;width:430px}
.about-cta{left:660px;top:370px}

/* services */
.services{top:1212px;height:548px;background:var(--beige)}
.services .section-title{top:84px}
.services .lead{position:absolute;top:132px;width:100%;text-align:center}
.service-cards{position:absolute;left:128px;top:188px;display:flex;gap:16px}
.service-card{width:224px;height:248px;border-radius:24px;overflow:hidden;position:relative}
.service-card .photo{position:absolute;inset:0}
.service-card .label{position:absolute;left:0;right:0;bottom:0;height:64px;background:var(--green);color:var(--white);font-weight:800;font-size:11px;text-align:center;display:flex;align-items:center;justify-content:center;padding:0 16px;line-height:1.35}
.pager{position:absolute;display:flex;gap:10px}
.pager span{width:40px;height:40px;border-radius:50%;display:flex;align-items:center;justify-content:center}
.pager .p1{background:var(--green)}
.pager .p2{background:var(--yellow)}
.services .pager{left:552px;top:484px}

/* why choose */
.why{top:1760px;height:780px}
.why .section-title{top:106px}
.why-item{position:absolute;width:210px}
.why-item h4{font-size:11px;font-weight:800;margin-bottom:4px}
.why-item p{font-size:9px;line-height:1.5;color:var(--muted)}
.why-item.left{text-align:right}
.center-mark{position:absolute;left:470px;top:270px;width:260px;height:260px;border-radius:50%;background:var(--white);display:flex;flex-direction:column;align-items:center;justify-content:center;border:4px solid var(--yellow)}
.center-mark .brand-name{font-size:40px}
.center-mark .brand-sub{font-size:12px}

/* projects */
.projects{top:2540px;height:680px;background:var(--beige)}
.projects h2{position:absolute;left:128px;top:84px;font-weight:800;font-size:34px}
.projects .pager{left:978px;top:84px}
.tile{position:absolute;border-radius:6px}

/* testimonials */
.testimonials{top:3220px;height:520px;background:var(--beige)}
.testimonials h2{position:absolute;left:120px;top:120px;color:var(--white);font-weight:900;font-size:34px;line-height:1.15;width:300px}
.rating{position:absolute;left:120px;top:270px;color:var(--white)}
.rating .lbl{font-weight:800;font-size:13px;margin-bottom:6px}
.stars{color:var(--yellow);letter-spacing:2px}
.rating .stars{color:var(--white);font-size:22px}
.review{position:absolute;top:80px;width:330px;height:380px;border-radius:165px;background:var(--white);border:3px solid var(--yellow);text-align:center;padding:96px 40px 0}
.review .q{position:absolute;left:0;right:0;top:26px;font-size:80px;font-weight:900;color:var(--green);line-height:1}
.review p{font-size:11px;line-height:1.6;color:var(--muted)}
.review h5{margin-top:20px;font-size:13px;font-weight:800}
.review .stars{font-size:15px;margin-top:4px}

/* contact */
.contact{top:3740px;height:500px}
.contact h2{position:absolute;left:120px;top:60px;font-weight:900;font-size:34px}
.field{position:absolute;left:120px;width:380px;height:40px;border:1px solid var(--line);border-radius:4px;background:var(--white);font-size:10px;color:var(--muted);display:flex;align-items:center;gap:10px;padding:0 14px}
.field.msg{height:96px;align-items:flex-start;padding-top:12px}
.contact-cta{left:120px;top:408px}

/* footer */
.footer{top:4240px;height:476px}
.footer-brand{position:absolute;left:0;width:100%;top:50px;text-align:center}
.footer-brand .brand-name{font-size:36px}
.footer-brand .brand-sub{font-size:11px}
.footer-nav{position:absolute;top:170px;left:0;width:100%;display:flex;justify-content:center;gap:46px;font-size:11px;font-weight:600}
.footer-nav .active{color:var(--green-dark)}
.footer-rule{position:absolute;left:120px;width:960px;height:1px;background:var(--line)}
.contact-row{position:absolute;top:250px;left:210px;display:flex;gap:70px;font-size:11px;font-weight:600;align-items:center}
.contact-row div{display:flex;align-items:center;gap:10px}
.ic{width:34px;height:34px;border-radius:50%;background:var(--green);display:flex;align-items:center;justify-content:center}
.socials{position:absolute;top:252px;left:880px;display:flex;gap:10px}
.socials span{width:30px;height:30px;border-radius:50%;border:1px solid var(--line)}
.copyright{position:absolute;left:0;right:0;bottom:0;height:60px;background:var(--beige);display:flex;align-items:center;justify-content:center;font-size:10px;color:var(--muted);font-weight:600}
.to-top{position:absolute;right:40px;top:430px;width:34px;height:34px;border-radius:50%;background:var(--yellow);display:flex;align-items:center;justify-content:center}
</style>
</head>
<body>

<header class="hero">
  <div class="hero-photo" role="img" aria-label="Sunlit garden with a stone path winding across a lawn between shrubs and trees"></div>
  <svg class="abs" style="left:0;top:0" width="1200" height="660" aria-hidden="true">
    <polygon points="0,72 720,72 560,660 0,660" fill="#5a9e1f" opacity=".55"/>
  </svg>
  <div class="nav-bar"></div>
  <div class="brand-badge"><div class="brand-name">VARLOW</div><div class="brand-sub">LAWN CARE &amp; LANDSCAPING</div></div>
  <nav class="nav-links"><span class="active">HOME</span><span>SERVICES</span><span>ABOUT US</span><span>GALLERY</span><span>TESTIMONIALS</span><span>CONTACT US</span></nav>
  <div class="btn btn-green nav-cta">BOOK AN APPOINTMENT <span class="dot"><svg width="10" height="10" viewBox="0 0 10 10"><path d="M2 5h6M5 2l3 3-3 3" stroke="#4f9a1c" stroke-width="1.6" fill="none"/></svg></span></div>
  <h1 class="hero-title">TRANSFORM YOUR OUTDOORS WITH EXPERT LANDSCAPING SERVICES</h1>
  <p class="hero-sub">FROM LAWN CARE TO COMPLETE YARD TRANSFORMATIONS — WE'VE GOT YOU COVERED!</p>
  <div class="btn btn-yellow hero-cta">GET A FREE QUOTE <span class="dot"><svg width="10" height="10" viewBox="0 0 10 10"><path d="M2 5h6M5 2l3 3-3 3" stroke="#1f2a1a" stroke-width="1.6" fill="none"/></svg></span></div>
  <div class="slider-dots"><span></span><span></span><span></span></div>
</header>

<section class="about">
  <div class="about-photo" role="img" aria-label="Landscaper pushing a lawn mower across a striped lawn"></div>
  <div class="about-photo-sm" role="img" aria-label="Freshly cut green lawn with a hedge"></div>
  <h2 class="about-title"><span class="hl">WELCOME VARLOW</span><br>MEET THE EXPERTS BEHIND</h2>
  <p class="about-text small">We are a husband and wife team passionate about creating beautiful outdoor spaces for every home. With care in every detail, we keep lawns healthy and yards tidy all season long. Our goal is simple: honest work, fair prices and results you can see from the street. From weekly mowing to full clean ups, we treat your yard like our own.</p>
  <div class="btn btn-green about-cta">READ MORE <span class="dot"><svg width="10" height="10" viewBox="0 0 10 10"><path d="M2 5h6M5 2l3 3-3 3" stroke="#4f9a1c" stroke-width="1.6" fill="none"/></svg></span></div>
</section>

<section class="services">
  <h2 class="section-title">OUR SERVICES</h2>
  <p class="lead small">Professional landscaping services tailored to your needs</p>
  <div class="service-cards">
    <div class="service-card"><div class="photo" role="img" aria-label="Riding mower on a lawn" style="background:linear-gradient(160deg,#6f9e3a,#2f5d16)"></div><div class="label">WEEKLY / BI-WEEKLY MOWING</div></div>
    <div class="service-card"><div class="photo" role="img" aria-label="Trimmer edging along a lawn border" style="background:linear-gradient(160deg,#9abf58,#3c6e1b)"></div><div class="label">WEED EATING &amp; EDGING</div></div>
    <div class="service-card"><div class="photo" role="img" aria-label="Gardener planting flowers in a bed" style="background:linear-gradient(160deg,#7fae48,#46721f)"></div><div class="label">PLANT INSTALLATION</div></div>
    <div class="service-card"><div class="photo" role="img" aria-label="Shrubs surrounded by fresh mulch" style="background:linear-gradient(160deg,#8aa84a,#5a4a2a)"></div><div class="label">PINESTRAW &amp; MULCH INSTALLATION</div></div>
  </div>
  <div class="pager"><span class="p1"><svg width="12" height="12" viewBox="0 0 12 12"><path d="M8 2L4 6l4 4" stroke="#fff" stroke-width="1.8" fill="none"/></svg></span><span class="p2"><svg width="12" height="12" viewBox="0 0 12 12"><path d="M4 2l4 4-4 4" stroke="#1f2a1a" stroke-width="1.8" fill="none"/></svg></span></div>
</section>

<section class="why">
  <h2 class="section-title">WHY CHOOSE VARLOW</h2>
  <svg class="abs" style="left:0;top:0" width="1200" height="780" aria-hidden="true">
    <circle cx="600" cy="400" r="220" fill="none" stroke="#7cbf2f" stroke-width="2" stroke-dasharray="6 6"/>
    <g fill="#7cbf2f">
      <circle cx="440" cy="250" r="34"/><circle cx="760" cy="250" r="34"/>
      <circle cx="380" cy="400" r="34"/><circle cx="820" cy="400" r="34"/>
      <circle cx="440" cy="550" r="34"/><circle cx="760" cy="550" r="34"/>
      <circle cx="600" cy="620" r="34"/>
    </g>
    <g stroke="#fff" stroke-width="2.4" fill="none" stroke-linecap="round" stroke-linejoin="round">
      <path d="M440 236l12 5v9c0 8-6 13-12 15-6-2-12-7-12-15v-9z"/><path d="M434 250l5 5 8-8"/>
      <path d="M760 236c-9 8-9 20 0 28 9-8 9-20 0-28zM760 250v16"/>
      <circle cx="380" cy="400" r="13"/><path d="M380 392v8l5 4"/>
      <path d="M808 402l12-14 12 14v10h-24z"/><path d="M815 402l4 4 7-7"/>
      <path d="M428 552l12-12 12 12v12h-24z"/><path d="M436 564v-8h8v8"/>
      <path d="M748 540h24v20h-24z"/><path d="M752 548h16M752 554h10"/>
      <circle cx="600" cy="612" r="6"/><path d="M588 634c2-8 22-8 24 0"/>
    </g>
  </svg>
  <div class="center-mark"><div class="brand-name">VARLOW</div><div class="brand-sub">LAWN CARE &amp; LANDSCAPING</div></div>
  <div class="why-item left" style="left:186px;top:222px"><h4>LICENSED AND INSURED</h4><p>We are a husband and wife team passionate about quality</p></div>
  <div class="why-item" style="left:806px;top:222px"><h4>PROFESSIONAL WORK</h4><p>We are a husband and wife team passionate about quality</p></div>
  <div class="why-item left" style="left:126px;top:374px"><h4>24 HOUR EMERGENCY SERVICES</h4><p>We are a husband and wife team passionate about quality</p></div>
  <div class="why-item" style="left:866px;top:374px"><h4>SAFETY IS OUR TOP PRIORITY</h4><p>We are a husband and wife team passionate about quality</p></div>
  <div class="why-item left" style="left:186px;top:524px"><h4>LOCALLY OWNED &amp; OPERATED</h4><p>We are a husband and wife team passionate about quality</p></div>
  <div class="why-item" style="left:806px;top:524px"><h4>FREE ESTIMATES</h4><p>We are a husband and wife team passionate about quality</p></div>
  <div class="why-item" style="left:495px;top:668px;text-align:center"><h4>LICENSED ARBORIST ON STAFF</h4><p>We are a husband and wife team passionate about quality</p></div>
</section>

<section class="projects">
  <h2>OUR RECENT PROJECTS</h2>
  <div class="pager"><span class="p1"><svg width="12" height="12" viewBox="0 0 12 12"><path d="M8 2L4 6l4 4" stroke="#fff" stroke-width="1.8" fill="none"/></svg></span><span class="p2"><svg width="12" height="12" viewBox="0 0 12 12"><path d="M4 2l4 4-4 4" stroke="#1f2a1a" stroke-width="1.8" fill="none"/></svg></span></div>
  <div class="tile" role="img" aria-label="Flower garden with colourful blooms and a lawn" style="left:128px;top:180px;width:232px;height:200px;background:linear-gradient(150deg,#a2c65a,#d07a9a 50%,#4d7a22)"></div>
  <div class="tile" role="img" aria-label="Freshly mowed lawn" style="left:372px;top:180px;width:232px;height:200px;background:linear-gradient(150deg,#6fae2f,#3d7a16)"></div>
  <div class="tile" role="img" aria-label="Gardener planting in a bed beside a lawn" style="left:128px;top:392px;width:232px;height:200px;background:linear-gradient(150deg,#8fbf4a,#5b4a2c)"></div>
  <div class="tile" role="img" aria-label="Trees lining a green lawn" style="left:372px;top:392px;width:232px;height:200px;background:linear-gradient(150deg,#7c9a5a,#2f5d16)"></div>
  <div class="tile" role="img" aria-label="Landscaper in orange cap trimming a hedge" style="left:616px;top:180px;width:456px;height:412px;background:linear-gradient(150deg,#4f7f24,#9cbc4a 55%,#e08a2a)"></div>
</section>

<section class="testimonials">
  <svg class="abs" style="left:0;top:0" width="1200" height="520" aria-hidden="true">
    <polygon points="0,0 460,0 360,520 0,520" fill="#f5c518"/>
  </svg>
  <h2>WHAT OUR CLIENTS ARE SAYING</h2>
  <div class="rating"><div class="lbl">EXCELLENT SERVICE</div><div class="stars">★★★★★</div><div style="font-size:9px;margin-top:6px;font-weight:600">BASED ON 120 REVIEWS</div></div>
  <div class="review" style="left:360px"><div class="q">“</div><p>"Excellent service! Our yard looks amazing thanks to Varlow. The team was professional, punctual, and extremely thorough. They really transformed our space into something we love spending time in!"</p><h5>OWEN &amp; CLARA R.</h5><div class="stars">★★★★★</div></div>
  <div class="review" style="left:720px"><div class="q">“</div><p>"We hired them for regular mowing, leaf cleanup, and seasonal yard maintenance. They've always gone above and beyond, leaving our yard looking pristine and well cared for. Highly recommended!"</p><h5>DEAN &amp; MIA W.</h5><div class="stars">★★★★★</div></div>
  <div class="review" style="left:1080px"><div class="q">“</div><p>"We hired them for seasonal cleanup and they did a wonderful job."</p></div>
</section>

<section class="contact">
  <svg class="abs" style="left:0;top:0" width="1200" height="500" aria-hidden="true">
    <polygon points="640,0 1200,0 1200,470 560,470" fill="#7cbf2f"/>
  </svg>
  <div class="abs" role="img" aria-label="Landscaper in orange cap kneeling to plant flowers" style="left:740px;top:0;width:460px;height:440px;background:linear-gradient(150deg,#5c8c2a,#a6c85a 50%,#e58a2a);clip-path:polygon(90px 0,460px 0,460px 440px,0 440px)"></div>
  <h2>CONTACT US</h2>
  <div class="field" style="top:140px">FIRST NAME</div>
  <div class="field" style="top:192px">EMAIL ADDRESS</div>
  <div class="field" style="top:244px">PHONE NUMBER</div>
  <div class="field msg" style="top:296px">YOUR MESSAGE</div>
  <div class="btn btn-green contact-cta">SEND MESSAGE <span class="dot"><svg width="10" height="10" viewBox="0 0 10 10"><path d="M2 5h6M5 2l3 3-3 3" stroke="#4f9a1c" stroke-width="1.6" fill="none"/></svg></span></div>
</section>

<footer class="footer">
  <div class="footer-brand"><div class="brand-name">VARLOW</div><div class="brand-sub">LAWN CARE &amp; LANDSCAPING</div></div>
  <div class="footer-rule" style="top:150px"></div>
  <nav class="footer-nav"><span class="active">HOME</span><span>SERVICES</span><span>ABOUT US</span><span>GALLERY</span><span>TESTIMONIALS</span><span>CONTACT US</span></nav>
  <div class="footer-rule" style="top:214px"></div>
  <div class="contact-row">
    <div><span class="ic"><svg width="14" height="14" viewBox="0 0 14 14"><path d="M3 1l2 3-1.5 1.5a8 8 0 0 0 5 5L10 9l3 2-1 2c-6 0-11-5-11-11z" fill="#fff"/></svg></span>(555) 014-2290</div>
    <div><span class="ic"><svg width="14" height="14" viewBox="0 0 14 14"><rect x="1" y="3" width="12" height="8" fill="none" stroke="#fff" stroke-width="1.5"/><path d="M1 3l6 5 6-5" fill="none" stroke="#fff" stroke-width="1.5"/></svg></span>hello@varlowyard.com</div>
    <div><span class="ic"><svg width="14" height="14" viewBox="0 0 14 14"><path d="M7 13S2 8 2 5a5 5 0 0 1 10 0c0 3-5 8-5 8z" fill="#fff"/><circle cx="7" cy="5" r="1.8" fill="#7cbf2f"/></svg></span>48 Fernbrook Lane, Milltown</div>
  </div>
  <div class="socials"><span></span><span></span><span></span><span></span></div>
  <div class="to-top"><svg width="12" height="12" viewBox="0 0 12 12"><path d="M2 8l4-4 4 4" stroke="#1f2a1a" stroke-width="1.8" fill="none"/></svg></div>
  <div class="copyright">© 2024 VARLOW. ALL RIGHTS RESERVED</div>
</footer>

</body>
</html>
```